Lindenfall Studio Business cards

Design our business cards and eventually a logo. The company is based in Paris, its activity is the retailing via internet of luxury home furniture (like Vantorelli, Bercasso, fradusi...) Our clients are international andwith a high sense of aesthetics. The design shall communicate wealth and trust with a high quality and aesthetic sense, pure lines Company Name is Lindenfall StudioExplanation of the name: usually people who wants to buy furniture usually go in a showroom. Today they go in showroom to test the furniture and they search for the price on internet, which is a "Lindenfall studio".We will not be a e-commerce site. Our site will be (another project) a presentation site which purpose is to reach qualified prospects. Then everything will be handled by phone, meeting etc.The business card must be professional as we will negotiate with many luxury brands, opportunity to represent them on our site, prices etc.As far as the color are concerned mostly black and whithe or grey. The font of the Lindenfall Studio name shall have some impact.

Target Market(s)

High-end furniture and buyers of luxury goods, international customers, mostly women who handle such projects.
We also deal with professional buyers (hotels as an example) and luxury brands

Contact Information for Business Card

standard format 85x55, lanscape card, square corners will be printed on thick high quality paper (300 or 350g)

Font styles to use
Sans Serif

Colors

Designer to choose colors to be used in the design.

Requirements
Must have
• Must be white, as the paper will be high quality, the paper will enhance the card.
• Name of the brand Lindenfall studio (with specific font which make it very nice looking and catch the attention. similar to Calibri or Calibri
• Name of person (will give you the name later (4 names and position)
• the position of the person
• Mobile phone, e-mail, Physical address 27, rue Caldenois, 75005 Paris, France (courrier only) our web site www.lindenfallstudio-example.fr
• The card must be simple and class
Nice to have
• Font of the address is smaller than the rest,
• Calibri font or similar on recto side with the name of the company which may look similar to the picture inserted in the brief.
• The grey color in the picture inserted is ok for us
Should not have
• Any parallel lines which represent the name of the company
• Any heavy design If you go on internet sites which present the furniture all designs are pure lines and high quality craftsmanship. To have an idea of our targetted client or brand we will be in touch: https://www.casavornetta-example.it/projects/
• Note that the picture added below is what we use, now as mail signature, up to you to have a better design etc.

```html
<!DOCTYPE html>
<html lang="en">
<head>
<meta charset="utf-8">
<title>Lindenfall Studio – Business cards</title>
<link href="https://fonts.googleapis.com/css2?family=Carlito:wght@400;700&display=swap" rel="stylesheet">
<style>
  :root {
    --backdrop: #ececea;
    --card-front: #e5e4e0;
    --card-back: #272727;
    --ink-grey: #656565;
    --ink-deep: #1c1c1c;
  }
  * { margin: 0; padding: 0; box-sizing: border-box; }
  html, body {
    width: 1200px;
    height: 1028px;
    overflow: hidden;
    background: var(--backdrop);
    font-family: "Carlito", "Calibri", sans-serif;
  }
  .canvas { position: relative; width: 1200px; height: 1028px; }
  .card {
    position: absolute;
    left: 310px;
    width: 580px;
    height: 330px;
  }
  .card--front { top: 166px; background: var(--card-front); color: var(--ink-grey); }
  .card--back { top: 532px; background: var(--card-back); }

  .company-name {
    position: absolute;
    left: 35px;
    top: 44px;
    font-size: 28px;
    font-weight: 700;
    letter-spacing: 0.1px;
  }
  .website {
    position: absolute;
    left: 35px;
    top: 270px;
    font-size: 17px;
  }
  .contact {
    position: absolute;
    left: 362px;
    top: 140px;
  }
  .person-name {
    font-size: 22px;
    font-weight: 700;
    letter-spacing: 0.6px;
    line-height: 26px;
  }
  .person-role {
    font-size: 18px;
    line-height: 22px;
  }
  .divider {
    width: 27px;
    height: 1.5px;
    background: var(--ink-grey);
    margin: 20px 0 22px;
  }
  .details {
    font-size: 17px;
    line-height: 22px;
    font-style: normal;
  }
  .back-mark {
    position: absolute;
    inset: 0;
    display: flex;
    align-items: center;
    justify-content: center;
    font-size: 37px;
    font-weight: 700;
    color: var(--ink-deep);
    padding-bottom: 6px;
  }
</style>
</head>
<body>
<main class="canvas">
  <section class="card card--front">
    <h1 class="company-name">Lindenfall Studio</h1>
    <div class="contact">
      <p class="person-name">MAREL DOSVIN</p>
      <p class="person-role">President / Co-Founder</p>
      <div class="divider"></div>
      <address class="details">
        +33612480937<br>
        27 rue Caldenois<br>
        75005 Paris, France
      </address>
    </div>
    <p class="website">www.lindenfallstudio-example.fr</p>
  </section>
  <section class="card card--back">
    <p class="back-mark">Lindenfall Studio</p>
  </section>
</main>
</body>
</html>
```